A building General Contractor is looking for a business card design

I need a business card designed. The company "Stoneridge Framing Contractors" is a general contractor for commercial buildings and pre-engineered metal buildings.

```html
<!DOCTYPE html>
<html lang="en">
<head>
<meta charset="utf-8">
<title>Stoneridge Framing Contractors – Business Card</title>
<link rel="stylesheet" href="https://fonts.googleapis.com/css2?family=Arimo:wght@400;700&display=swap">
<style>
  :root {
    --page-bg: #e4e4e2;
    --card-bg: #232325;
    --card-bg-back: #1f1f21;
    --ink-light: #f2f2f2;
    --ink-muted: #c9c9c9;
    --rule: #bdbdbd;
    --emboss: #3a3a3d;
  }
  * { margin: 0; padding: 0; box-sizing: border-box; }
  html, body {
    width: 1200px; height: 801px; overflow: hidden;
    background: var(--page-bg);
    font-family: "Arimo", Arial, sans-serif;
  }
  .sheet {
    width: 1200px; height: 801px;
    display: flex; align-items: center; justify-content: center; gap: 48px;
  }
  .card {
    width: 540px; height: 309px;
    position: relative;
    box-shadow: 0 10px 24px rgba(0,0,0,.22);
  }
  .card--front { background: var(--card-bg); color: var(--ink-light); }
  .card--back  { background: var(--card-bg-back); display: flex; align-items: center; justify-content: center; }

  .brand {
    position: absolute; top: 42px; right: 40px;
    display: flex; align-items: center; gap: 12px;
  }
  .brand__mark { width: 16px; height: 16px; background: var(--ink-light); }
  .brand__name {
    font-weight: 700; font-size: 19px; line-height: 1.15;
    text-transform: uppercase; letter-spacing: .04em; text-align: left;
    color: var(--ink-light);
  }
  .card--back .brand { position: static; }
  .card--back .brand__mark { background: var(--emboss); width: 22px; height: 22px; }
  .card--back .brand__name { color: var(--emboss); font-size: 26px; }

  .divider {
    position: absolute; left: 40px; right: 40px; top: 170px;
    height: 1px; background: var(--rule);
  }
  .person { position: absolute; left: 40px; top: 124px; }
  .person__name { font-weight: 700; font-size: 18px; letter-spacing: .03em; text-transform: uppercase; }
  .person__role { font-size: 12px; color: var(--ink-muted); margin-top: 3px; }

  .contacts {
    position: absolute; left: 40px; top: 186px;
    list-style: none; font-size: 13px; line-height: 1.9; color: var(--ink-light);
  }
  .contacts li { display: flex; align-items: center; gap: 9px; }
  .contacts svg { width: 12px; height: 12px; flex: none; }
  .contacts .icon-fill { fill: var(--ink-light); }
  .contacts .icon-line { fill: none; stroke: var(--ink-light); stroke-width: 2; }

  .address {
    position: absolute; right: 40px; top: 190px;
    font-size: 12.5px; line-height: 1.5; text-align: right; color: var(--ink-muted);
  }
</style>
</head>
<body>
<main class="sheet">
  <section class="card card--front" aria-label="Card front">
    <div class="brand">
      <span class="brand__mark"></span>
      <div class="brand__name">Stoneridge Framing<br>Contractors</div>
    </div>

    <div class="person">
      <h1 class="person__name">Marcus Hale</h1>
      <p class="person__role">Manager</p>
    </div>

    <div class="divider"></div>

    <ul class="contacts">
      <li>
        <svg viewBox="0 0 24 24" aria-hidden="true"><path class="icon-fill" d="M6.6 10.8a15 15 0 0 0 6.6 6.6l2.2-2.2c.3-.3.7-.4 1-.2 1.1.4 2.3.6 3.6.6.6 0 1 .4 1 1V20c0 .6-.4 1-1 1A17 17 0 0 1 3 4c0-.6.4-1 1-1h3.5c.6 0 1 .4 1 1 0 1.3.2 2.5.6 3.6.1.3 0 .7-.2 1z"/></svg>
        555-014-2736
      </li>
      <li>
        <svg viewBox="0 0 24 24" aria-hidden="true"><path class="icon-fill" d="M2 5h20v14H2zm2 2v.5l8 5 8-5V7zm0 2.8V17h16V9.8l-8 5z"/></svg>
        youremail@mailbox.com
      </li>
      <li>
        <svg viewBox="0 0 24 24" aria-hidden="true"><g class="icon-line"><circle cx="12" cy="12" r="9"/><ellipse cx="12" cy="12" rx="4" ry="9"/><path d="M3 12h18"/></g></svg>
        www.yourwebsite.com
      </li>
    </ul>

    <p class="address">Your address, city<br>state, ZIP 0000</p>
  </section>

  <section class="card card--back" aria-label="Card back">
    <div class="brand">
      <span class="brand__mark"></span>
      <div class="brand__name">Stoneridge Framing<br>Contractors</div>
    </div>
  </section>
</main>
</body>
</html>
```